Custom Bladeless LASIK Poster Design Project

I would like a poster whose theme will also be used for future brochures. I would also like it to be created in such a way that it can be part of an in-office branding campaign. Our company already has a logo. We are the premier Ophthalmology group in Orange County, NY specializing in Cataract and Laser Refractive surgery. This particular poster should highlight the advantages to Custom Bladeless LASIK and mention our free consultations and website www.brightmorrowsight.com
Updates

Would like to make sure the color palette complements the colors in our logo.   Also try incorporating the phrase "Regain your Sight, Regain your Life"

The message should also invite the patient to inquire about more information or to tell a friend about our services

just uploaded the full zip file, please try again.

I just uploaded the full zip file for our logo.  Please let me know if there is still a problem.  Thanks

poster size should be 24" wide 32" high

and able to reduce it to 18"W x 24"H

Thank you 
The designer I choose will also be used in near future for other poster and in office materials highlighting our other services

Reason: I would like to give the other designers that accepted our invitation an opportunity to submit a design.

Industry/Entity Type

It Company

Requirements
Must have
• attractive young and active male or female model extolling the virtues of eliminating there glasses and contact lenses.

```html
<!DOCTYPE html>
<html lang="en">
<head>
<meta charset="utf-8">
<title>Custom Bladeless LASIK – Brightmorrow Sight</title>
<link rel="stylesheet" href="https://fonts.googleapis.com/css2?family=Arimo:wght@400;700&family=Exo+2:wght@300&family=Tinos&display=swap">
<style>
  :root {
    --wine: #7a1f1b;
    --wine-deep: #4b1915;
    --panel-top: #57201b;
    --panel-bottom: #8c2b23;
    --ink: #1b1b1b;
    --paper: #ffffff;
    --guide: #bfe3ec;
    --skin-light: #f6ece6;
    --skin-warm: #e8c9b4;
    --hair: #d9b889;
  }
  html, body {
    margin: 0;
    padding: 0;
    overflow: hidden;
    background: var(--paper);
  }
  .poster {
    position: relative;
    width: 855px;
    height: 1200px;
    overflow: hidden;
    background: var(--paper);
    font-family: "Arimo", Arial, sans-serif;
  }
  .trim-guide {
    position: absolute;
    left: 15px; top: 17px; right: 15px; bottom: 15px;
    border: 1px solid var(--guide);
  }
  .hero-photo {
    position: absolute;
    left: 0; top: 0;
    width: 474px; height: 421px;
    background:
      radial-gradient(ellipse 55% 60% at 45% 45%, var(--skin-light) 0%, var(--skin-warm) 55%, transparent 75%),
      linear-gradient(120deg, var(--hair) 0%, #f3e7dc 45%, #fbf6f2 100%);
    box-shadow: 0 8px 10px -4px rgba(90, 50, 20, 0.55);
  }
  .headline-panel {
    position: absolute;
    left: 474px; top: 0;
    width: 381px; height: 421px;
    background: linear-gradient(180deg, var(--panel-top), var(--panel-bottom));
  }
  .headline-panel p {
    margin: 0;
    position: absolute;
    left: 24px;
    font-family: "Exo 2", "Trebuchet MS", sans-serif;
    font-weight: 300;
    font-size: 76px;
    line-height: 1;
    color: var(--paper);
  }
  .headline-panel .line-1 { top: 44px; }
  .headline-panel .line-2 { top: 160px; }
  .headline-panel .line-3 { top: 276px; }
  .offer-bar {
    position: absolute;
    left: 474px; top: 421px;
    width: 381px; height: 68px;
    background: var(--wine-deep);
    color: var(--paper);
    font-family: "Exo 2", "Trebuchet MS", sans-serif;
    font-weight: 300;
    font-size: 32px;
    letter-spacing: 1px;
    line-height: 68px;
    text-align: center;
  }
  .title-lasik {
    position: absolute;
    left: 0; width: 855px;
    top: 500px;
    margin: 0;
    text-align: center;
    font-weight: 400;
    font-size: 284px;
    line-height: 1;
    letter-spacing: -4px;
    color: var(--ink);
    -webkit-text-stroke: 4px var(--wine);
    paint-order: stroke fill;
  }
  .title-freedom {
    position: absolute;
    right: 24px;
    top: 778px;
    margin: 0;
    font-weight: 400;
    font-size: 158px;
    line-height: 1;
    color: var(--wine);
    -webkit-text-stroke: 1.5px var(--ink);
  }
  .tagline {
    position: absolute;
    left: 0; width: 855px;
    top: 926px;
    margin: 0;
    text-align: center;
    font-weight: 700;
    font-size: 40px;
    letter-spacing: -0.2px;
    color: var(--ink);
  }
  .contact-bar {
    position: absolute;
    left: 0; top: 1017px;
    width: 855px; height: 42px;
    background: var(--wine);
    color: var(--paper);
    font-family: "Exo 2", "Trebuchet MS", sans-serif;
    font-weight: 300;
    font-size: 25px;
    letter-spacing: 1px;
    line-height: 42px;
    text-align: center;
  }
  .doctor {
    position: absolute;
    left: 18px; top: 1068px;
    width: 240px;
    text-align: center;
  }
  .doctor-portrait {
    display: block;
    width: 54px; height: 58px;
    margin: 0 auto 6px;
    background: linear-gradient(180deg, #c9c9cc 0%, #8d8f95 60%, #3c3e44 100%);
  }
  .doctor-name {
    margin: 0;
    font-family: "Tinos", "Times New Roman", serif;
    font-size: 22px;
    color: var(--ink);
  }
  .doctor-tagline {
    margin: 1px 0 0;
    font-family: "Tinos", "Times New Roman", serif;
    font-size: 11px;
    color: var(--wine);
  }
  .contact-details {
    position: absolute;
    left: 270px; top: 1122px;
    width: 310px;
    text-align: center;
    font-family: "Exo 2", "Trebuchet MS", sans-serif;
    font-weight: 300;
    font-size: 17px;
    line-height: 27px;
    color: var(--ink);
  }
  .contact-details p { margin: 0; }
  .practice-name {
    position: absolute;
    left: 590px; top: 1122px;
    width: 250px;
    display: flex;
    align-items: center;
    justify-content: center;
    gap: 10px;
    font-weight: 700;
    font-size: 22px;
    color: var(--wine);
  }
  .practice-mark {
    width: 16px; height: 16px;
    border-radius: 50%;
    background: var(--wine);
  }
</style>
</head>
<body>
  <main class="poster">
    <div class="trim-guide"></div>

    <div class="hero-photo" role="img" aria-label="Photo of a smiling young woman with blonde hair and clear eyes, free of glasses"></div>

    <section class="headline-panel">
      <p class="line-1">Custom</p>
      <p class="line-2">Bladeless</p>
      <p class="line-3">LASIK</p>
    </section>
    <div class="offer-bar">Free Consultations</div>

    <h1 class="title-lasik">LASIK</h1>
    <h2 class="title-freedom">Freedom</h2>
    <p class="tagline">"Regain your Sight, Regain your Life"</p>

    <div class="contact-bar">GET IN TOUCH</div>

    <div class="doctor">
      <span class="doctor-portrait" role="img" aria-label="Portrait photo of the surgeon"></span>
      <p class="doctor-name">Dr. Daniel Marlowe</p>
      <p class="doctor-tagline">Eye Care Excellence in the Hudson Valley</p>
    </div>

    <div class="contact-details">
      <p>845.555.0192</p>
      <p>INFO@BRIGHTMORROWSIGHT.COM</p>
    </div>

    <div class="practice-name">
      <span class="practice-mark"></span>
      <span>Brightmorrow Sight</span>
    </div>
  </main>
</body>
</html>
```